Hardcore nerd needs to stand out in a sea of dull Defence business cards

Wombat Devices is a new Australian consulting engineering company that turns research and theory into practical systems. No evangelistic fluff, just mathematics and physics into electronic and optical circuits for consumer products, scientific research or Defence applications.

We already have a recognised logo (provided) which is often dark blue/black on a light background but we're open to other combinations. (Us engineers tend to have limited aesthetic imagination :)

Some of our recent products have included:
* Instrumentation for electrical testing,
* Radar jammers,
* GPS antenna design,
* Satellite tracking systems,
* High power lasers

We're open to both single and double-sided designs - happy to be convinced either way.

P.S. Another group is working on the web page, so - alas - our web site is currently of no use for images/ideas...

Target Market(s)

Engineering managers,
Scientists

Contact Information for Business Card

Dr Colin Marsh
R&D Engineer

colin@wombatdevicesco.com.au
0427 563 210

PO Box XXX (to be confirmed)
Banks ACT 2913
Australia

Font styles to use
Serif
Sans Serif

Colors

Designer to choose colors to be used in the design.

Requirements
Must have
• My contact details!
• I've had many (great) "bold and plain" designs submitted already, so feel free to be artistically creative :)
• Happy to take advice re fonts/colours/printability etc.
Nice to have
• I'm not sure if "lists" are more at home on a CV than a business card, but representative services include:
• Applied electromagnetics
• RF and high speed electronics
• Signal and image processing
• Electro-optical and laser systems
• Concept-to-prototype design services
• If you're considering double sided cards, then often measuring/alignment grids/rulers feature on the back of similar cards.
• e.g. https://www.lumoptix-example.com/newgrouppage9.cfm?objectgroup_id=4815
• https://www.lumoptix-example.com/newgrouppage9.cfm?objectgroup_ID=4817
• ..or even a "Smith chart" (google will return lots)
• Generic images to represent a capability might work - googling images associated with keyword for each of these areas might help:
• - "passive radar", "phased array", "fdtd", "vircator"
• RF and high speed electronic design
• - "smith chart", "microstrip circuits", "dimensioned drawing", "electronic schematic"
• - "dft", "iir filter"
• - "optical cavity". "laser energy level diagram"
• Background/watermarked images outlines/wireframes/schematics would probably look OK.
Should not have
• If a list of projects/services is provided, it is important not to make the client feel that this is "all" the company can do. Engineering design is a creative discipline (like graphics :)
• Please, no stock "military" snaps like planes, missiles, etc!

```html
<!DOCTYPE html>
<html lang="en">
<head>
<meta charset="utf-8">
<title>Wombat Devices – Business Card</title>
<link href="https://fonts.googleapis.com/css2?family=Oswald:wght@500&family=Roboto:wght@400;500&display=swap" rel="stylesheet">
<style>
  :root {
    --backdrop: #0d0d0d;
    --backdrop-glow: #2a2a2a;
    --card: #1b1b1b;
    --card-edge: #242424;
    --silver: #cfcfcf;
    --silver-dim: #9a9a9a;
    --silver-muted: #7c7c7c;
  }
  * { box-sizing: border-box; margin: 0; padding: 0; }
  html, body { width: 1200px; height: 900px; overflow: hidden; }
  body {
    background: radial-gradient(ellipse at 50% 35%, var(--backdrop-glow) 0%, var(--backdrop) 70%);
    font-family: "Roboto", Arial, sans-serif;
    color: var(--silver);
  }
  .card {
    position: absolute;
    left: 280px;
    width: 640px;
    height: 366px;
    background: linear-gradient(135deg, var(--card-edge) 0%, var(--card) 55%, #151515 100%);
    box-shadow: 0 18px 40px rgba(0,0,0,0.6);
  }
  .card--front { top: 68px; }
  .card--back { top: 466px; }

  /* Front */
  .brand {
    position: absolute;
    top: 92px;
    left: 0; right: 0;
    display: flex;
    justify-content: center;
    align-items: center;
    gap: 16px;
  }
  .brand-dot {
    width: 64px; height: 64px;
    border-radius: 50%;
    background: var(--silver);
  }
  .brand-name {
    font-family: "Roboto", Arial, sans-serif;
    font-weight: 500;
    font-size: 34px;
    letter-spacing: 2px;
    text-transform: uppercase;
    color: var(--silver);
  }
  .services {
    position: absolute;
    top: 208px;
    left: 0; right: 0;
    text-align: center;
    font-size: 17px;
    line-height: 24px;
    color: var(--silver-dim);
    list-style: none;
  }

  /* Back */
  .person {
    position: absolute;
    top: 128px;
    left: 52px;
    width: 250px;
    text-align: right;
  }
  .person-name {
    font-family: "Oswald", "Arial Narrow", sans-serif;
    font-weight: 500;
    font-size: 38px;
    line-height: 44px;
    letter-spacing: 1px;
    text-transform: uppercase;
    color: var(--silver-muted);
  }
  .person-role {
    font-size: 17px;
    color: var(--silver-dim);
    margin-top: 2px;
  }
  .divider {
    position: absolute;
    top: 128px;
    left: 326px;
    width: 2px;
    height: 74px;
    background: var(--silver-dim);
  }
  .contact {
    position: absolute;
    top: 130px;
    left: 348px;
    list-style: none;
    font-size: 17px;
    line-height: 24px;
    color: var(--silver);
  }
  .contact li { display: flex; align-items: center; gap: 10px; }
  .contact svg { width: 13px; height: 13px; flex: none; }
  .address {
    position: absolute;
    top: 292px;
    left: 30px;
    font-size: 17px;
    letter-spacing: 0.5px;
    color: var(--silver-dim);
  }
</style>
</head>
<body>
  <section class="card card--front">
    <div class="brand">
      <span class="brand-dot"></span>
      <span class="brand-name">Wombat Devices</span>
    </div>
    <ul class="services">
      <li>* Instrumentation for electrical testing,</li>
      <li>* Radar jammers, * GPS antenna design,</li>
      <li>* Satellite tracking systems, * High power lasers</li>
    </ul>
  </section>

  <section class="card card--back">
    <div class="person">
      <h1 class="person-name">Dr Colin Marsh</h1>
      <p class="person-role">R&amp;D Engineer</p>
    </div>
    <span class="divider"></span>
    <ul class="contact">
      <li>
        <svg viewBox="0 0 16 16" aria-hidden="true"><path fill="#cfcfcf" d="M3.6 1.2l2.2 2.6-1.3 1.6c.9 2 2.3 3.5 4.3 4.4l1.6-1.3 2.6 2.2-1.2 2.4C6.7 13 3 9.3 1.2 3.6z"/></svg>
        0427 563 210
      </li>
      <li>
        <svg viewBox="0 0 16 16" aria-hidden="true"><rect x="1.5" y="3.5" width="13" height="9" fill="none" stroke="#cfcfcf" stroke-width="1.4"/><path d="M1.5 3.5L8 9l6.5-5.5" fill="none" stroke="#cfcfcf" stroke-width="1.4"/></svg>
        colin@wombatdevicesco.com.au
      </li>
      <li>
        <svg viewBox="0 0 16 16" aria-hidden="true"><g fill="none" stroke="#cfcfcf" stroke-width="1.2"><circle cx="8" cy="8" r="6.3"/><ellipse cx="8" cy="8" rx="2.8" ry="6.3"/><path d="M1.7 8h12.6M2.8 4.6h10.4M2.8 11.4h10.4"/></g></svg>
        www.wombatdevicesco.com.au
      </li>
    </ul>
    <p class="address">PO Box XXX (to be confirmed) Banks ACT 2913 Australia</p>
  </section>
</body>
</html>
```